Large and Small Oval Label

This will be for a medium 2 1/2h x 3 1/2w oval, 8 oz.. and a small 1 1/2h x 2 1/2w oval, 4 oz.. Same Design and product information. Different sizes. My "old" label is attached. My logo, also attached, needs to be added. Sample information, attached with notes in Powerpoint.. Font type is the same as the "old" label. I do not want lines going across the oval like the "old" label. Natural color label.

Please note: The top edge on the "old" label that list the "cautions". I need this shift down to the bottom edge of the label instead of at the top.

Thanks!! m

Product

```html
<!DOCTYPE html>
<html lang="en">
<head>
<meta charset="utf-8">
<title>Willow Grove – Oval Product Label</title>
<link href="https://fonts.googleapis.com/css2?family=Satisfy&family=Cinzel:wght@400;700&display=swap" rel="stylesheet">
<style>
  :root {
    --page: #ffffff;
    --kraft: #c9a47c;
    --ink: #1c1a18;
  }
  html, body {
    margin: 0;
    width: 1200px;
    height: 900px;
    overflow: hidden;
    background: var(--page);
  }
  .label {
    display: block;
    width: 1200px;
    height: 900px;
  }
  .label-body { fill: var(--kraft); }
  .ring-outer { fill: none; stroke: var(--ink); stroke-width: 10; }
  .ring-inner { fill: none; stroke: var(--ink); stroke-width: 2; }
  .divider { stroke: var(--ink); stroke-width: 1.5; }
  .brand-mark { fill: none; stroke: var(--ink); stroke-width: 5; }
  .script { font-family: "Satisfy", cursive; fill: var(--ink); text-anchor: middle; }
  .brand-name { font-size: 62px; }
  .product-line { font-size: 92px; }
  .ampersand { font-size: 42px; }
  .tagline {
    font-family: "Cinzel", serif; font-size: 34px; fill: var(--ink);
    text-anchor: middle; letter-spacing: 1px;
  }
  .website {
    font-family: "Cinzel", serif; font-weight: 700; font-size: 27px; fill: var(--ink);
    text-anchor: middle; letter-spacing: 5px;
  }
  .net-weight {
    font-family: "Cinzel", serif; font-weight: 700; font-size: 20px; fill: var(--ink);
    text-anchor: middle; letter-spacing: 3px;
  }
  .caution {
    font-family: Arial, Helvetica, sans-serif; font-style: italic; font-size: 14px;
    fill: var(--ink); text-anchor: middle;
  }
</style>
</head>
<body>
<svg class="label" viewBox="0 0 1200 900" xmlns="http://www.w3.org/2000/svg" aria-label="Willow Grove oval product label">
  <ellipse class="label-body" cx="600" cy="450" rx="515" ry="376"/>
  <ellipse class="ring-outer" cx="600" cy="450" rx="499" ry="362"/>
  <ellipse class="ring-inner" cx="600" cy="450" rx="484" ry="348"/>

  <circle class="brand-mark" cx="600" cy="180" r="22"/>
  <text class="script brand-name" x="600" y="285">Willow Grove</text>

  <text class="script product-line" x="600" y="392">Natural Bath</text>
  <line class="divider" x1="272" y1="416" x2="556" y2="416"/>
  <line class="divider" x1="658" y1="416" x2="940" y2="416"/>
  <text class="script ampersand" x="600" y="458">&amp;</text>
  <text class="script product-line" x="600" y="520">Body Skin Therapy</text>

  <text class="tagline" x="600" y="575">Simply Authentic</text>
  <text class="website" x="600" y="636">WWW.WILLOWGROVESTORE.COM</text>
  <text class="net-weight" x="600" y="682">NET WT. 8 OZ.</text>

  <text class="caution" x="600" y="719">CAUTION: Lorem ipsum dolor sit. Lorem ispum dolor sit.</text>
  <text class="caution" x="600" y="738">Lorem ispum dolor sit.</text>
</svg>
</body>
</html>
```